Harbor Oak Electric website

I need a website for my electrical service business. We do a variety of electrical services for both commercial and residential clients in the Raleigh/Durham area of NC. I would like it to be done by someone who understands the electrical trade. I want a design that uses the color green in my logo. The design should communicate quality in electrical services for jobs big and small. It should have a button to call and a section to email requesting services. A place to list the time of services we offer as well. mobile friendly. First page should have a section for testimonials. A list of services will be provided. Only clean clear pictures. I will provide some.

```html
<!DOCTYPE html>
<html lang="en">
<head>
<meta charset="utf-8">
<title>Harbor Oak Electric</title>
<link rel="stylesheet" href="https://fonts.googleapis.com/css2?family=Orbitron:wght@700;900&family=Lato:wght@400;700&display=swap">
<style>
:root{
  --green:#1f9a3b;
  --green-dark:#187a2f;
  --black:#141414;
  --ink:#222;
  --text:#333;
  --grey:#f1f1f1;
  --white:#fff;
  --footer:#1b1b1b;
  --footer-bottom:#141414;
}
*{box-sizing:border-box;margin:0;padding:0}
html,body{width:1200px;height:3785px;overflow:hidden}
body{position:relative;font-family:'Lato',sans-serif;color:var(--text);background:var(--white)}
.abs{position:absolute}
.display{font-family:'Orbitron',sans-serif;font-weight:900;letter-spacing:2px;text-transform:uppercase}
.btn{position:absolute;display:flex;align-items:center;justify-content:center;background:var(--green);color:var(--white);font-family:'Orbitron',sans-serif;font-weight:700;font-size:14px;letter-spacing:1.5px;text-transform:uppercase}
.section-title{position:absolute;left:0;width:1200px;text-align:center;font-size:36px;color:var(--ink)}

/* header */
.brand{left:75px;top:34px}
.brand-name{font-family:'Lato',sans-serif;font-weight:700;font-size:38px;color:var(--ink);letter-spacing:1px;line-height:1}
.brand-sub{font-family:'Lato',sans-serif;font-weight:700;font-size:22px;color:var(--ink);letter-spacing:11px;margin-top:6px;padding-left:70px}
.header-phone{left:614px;top:54px;font-family:'Orbitron',sans-serif;font-weight:700;font-size:25px;color:var(--ink);display:flex;align-items:center;gap:12px}
.header-cta{left:947px;top:48px;width:180px;height:45px;font-size:15px}

/* nav */
.nav{left:0;top:141px;width:1200px;height:66px;background:var(--green);display:flex;padding-left:75px}
.nav a{color:var(--white);font-size:14px;font-weight:700;text-decoration:none;display:flex;align-items:center;padding:0 25px;text-transform:uppercase}
.nav a.active{background:var(--black)}

/* hero */
.hero{left:0;top:207px;width:1200px;height:642px;background:linear-gradient(100deg,#6f6f6f 0%,#8c8a86 40%,#6d6a5a 70%,#8a9646 100%)}
.hero-title{left:0;width:1200px;text-align:center;color:var(--white);font-size:70px;line-height:74px;top:375px}
.hero-sub{left:0;width:1200px;text-align:center;color:var(--white);font-size:25px;line-height:34px;top:534px}
.hero-btn{left:519px;top:623px;width:164px;height:47px}
.dots{left:563px;top:800px;display:flex;gap:10px}
.dots span{width:10px;height:10px;border-radius:50%;background:var(--white)}
.dots span.on{background:var(--green)}

/* services */
.card{position:absolute;top:978px;width:330px;height:384px;background:var(--grey);box-shadow:0 10px 12px -8px rgba(0,0,0,.25);text-align:center}
.card-photo{height:202px}
.card h3{font-family:'Orbitron',sans-serif;font-weight:900;font-size:18px;color:var(--green);letter-spacing:1px;margin-top:26px}
.card p{font-size:14px;line-height:23px;margin:16px 22px 0;color:var(--text)}
.card .btn{left:83px;top:359px;width:164px;height:47px;font-size:13px}
.arrow{position:absolute}

/* welcome */
.welcome-title{left:75px;top:1532px;color:var(--white);font-size:34px;line-height:44px;letter-spacing:3px}
.welcome-text{left:75px;top:1684px;width:470px;color:#e6e6e6;font-size:16px;line-height:30.5px}
.welcome-btn{left:75px;top:1866px;width:165px;height:47px}

/* what we do */
.checklist{position:absolute;top:2136px;list-style:none}
.checklist li{display:flex;align-items:center;gap:16px;height:36px;font-size:16px;color:var(--text)}
.checklist svg{flex:none}
.services-btn{left:474px;top:2474px;width:252px;height:47px}

/* testimonials */
.testimonials{left:0;top:2587px;width:1200px;height:524px;background:linear-gradient(180deg,#1e9539,#188a33)}
.testi-title{color:var(--white);top:2655px}
.testi{position:absolute;top:2741px;width:330px;text-align:center}
.testi-photo{width:176px;height:176px;border-radius:50%;margin:0 auto;background:radial-gradient(circle at 50% 40%,#d9c3b0,#ececec 70%)}
.testi h4{font-family:'Orbitron',sans-serif;font-weight:900;font-size:19px;color:var(--white);letter-spacing:1.5px;margin-top:22px}
.testi p{font-size:14px;line-height:23px;color:#eaf5ec;margin-top:12px}

/* subscribe */
.sub-title{top:3168px}
.sub-text{left:0;width:1200px;top:3229px;text-align:center;font-size:14px;color:var(--text)}
.sub-form{left:253px;top:3276px;width:692px;height:62px;display:flex;border:1px solid #cfcfcf}
.sub-input{flex:1;background:#f1f1f1;display:flex;align-items:center;gap:16px;padding-left:22px;font-size:13px;color:#555}
.sub-btn{position:static;width:145px;height:100%;font-size:17px}

/* footer */
.footer{left:0;top:3398px;width:1200px;height:307px;background:var(--footer)}
.footer-bottom{left:0;top:3705px;width:1200px;height:80px;background:var(--footer-bottom);border-top:1px solid #2c2c2c;color:#bbb;font-size:13px;text-align:center;padding-top:36px}
.f-head{font-family:'Orbitron',sans-serif;font-weight:700;font-size:15px;color:var(--white);letter-spacing:1.5px;top:3468px}
.f-list{list-style:none;top:3501px}
.f-list li{font-size:13px;color:#cfcfcf;height:31px}
.f-contact{left:615px;top:3501px;font-size:13px;color:#cfcfcf;line-height:24px}
.f-contact .name{color:var(--green);font-weight:700}
.f-contact .row{display:flex;align-items:center;gap:16px}
.socials{left:887px;top:3508px;display:flex;gap:22px}
.socials span{width:22px;height:22px;border-radius:50%;background:var(--white)}
.f-brand{left:884px;top:3590px;color:var(--white);font-weight:700;text-align:center;width:210px}
.f-brand .n{font-size:22px;letter-spacing:1px}
.f-brand .s{font-size:12px;letter-spacing:7px;margin-top:4px}
</style>
</head>
<body>

<!-- header -->
<div class="abs brand">
  <div class="brand-name">HARBOR OAK</div>
  <div class="brand-sub">ELECTRIC</div>
</div>
<div class="abs header-phone">
  <svg width="20" height="20" viewBox="0 0 24 24"><path fill="#222" d="M6.6 10.8a15.1 15.1 0 0 0 6.6 6.6l2.2-2.2c.3-.3.7-.4 1-.2 1.1.4 2.3.6 3.6.6.6 0 1 .4 1 1V20c0 .6-.4 1-1 1A17 17 0 0 1 3 4c0-.6.4-1 1-1h3.5c.6 0 1 .4 1 1 0 1.3.2 2.5.6 3.6.1.3 0 .7-.2 1z"/></svg>
  1-800-555-0142
</div>
<div class="btn header-cta">Contact Us</div>

<nav class="abs nav">
  <a class="active">Home</a><a>About Us</a><a>Services</a><a>Commercial</a><a>Residential</a><a>Testimonials</a><a>Blog</a><a>Contact Us</a>
</nav>

<!-- hero -->
<div class="abs hero" role="img" aria-label="Electrician in hard hat testing wiring in an electrical panel"></div>
<h1 class="abs display hero-title">Harbor Oak<br>Electric</h1>
<p class="abs hero-sub">Vestibulum ante ipsum primis in faucibus orci luctus<br>et ultrices posuere..</p>
<div class="btn hero-btn">Read More</div>
<div class="abs dots"><span class="on"></span><span></span><span></span><span></span></div>

<!-- service offers -->
<h2 class="display section-title" style="top:900px">Service Offers</h2>
<svg class="arrow" style="left:36px;top:1155px" width="24" height="40" viewBox="0 0 24 40"><path d="M20 2 3 20l17 18" fill="none" stroke="#333" stroke-width="3"/></svg>
<svg class="arrow" style="left:1140px;top:1155px" width="24" height="40" viewBox="0 0 24 40"><path d="m4 2 17 18L4 38" fill="none" stroke="#333" stroke-width="3"/></svg>

<div class="card" style="left:75px">
  <div class="card-photo" role="img" aria-label="Electrician in white hard hat using a multimeter" style="background:linear-gradient(135deg,#3b4650,#8c96a0 60%,#d6c24a)"></div>
  <h3>Doloremque</h3>
  <p>Vestibulum ante ipsum primis in faucibus orci luctus et ultrices posuere cubilia lobortis turpis in odio blandit..</p>
  <div class="btn">Read More</div>
</div>
<div class="card" style="left:435px">
  <div class="card-photo" role="img" aria-label="Electrician with clipboard beside a fuse board" style="background:linear-gradient(135deg,#6c6c6c,#d8d8d8 60%,#3b5fa8)"></div>
  <h3>Doloremque</h3>
  <p>Vestibulum ante ipsum primis in faucibus orci luctus et ultrices posuere cubilia lobortis turpis in odio blandit..</p>
  <div class="btn">Read More</div>
</div>
<div class="card" style="left:795px">
  <div class="card-photo" role="img" aria-label="Technician in orange workwear measuring a control panel" style="background:linear-gradient(135deg,#2d3a55,#c4502c 55%,#3a3a3a)"></div>
  <h3>Doloremque</h3>
  <p>Vestibulum ante ipsum primis in faucibus orci luctus et ultrices posuere cubilia lobortis turpis in odio blandit..</p>
  <div class="btn">Read More</div>
</div>

<!-- welcome -->
<svg class="abs" style="left:0;top:1454px" width="1200" height="547" viewBox="0 0 1200 547">
  <defs>
    <linearGradient id="welcomePhoto" x1="0" y1="0" x2="1" y2="0">
      <stop offset="0" stop-color="#3a5fc8"/><stop offset=".45" stop-color="#7d8fb8"/><stop offset=".8" stop-color="#8a7a68"/><stop offset="1" stop-color="#5a5550"/>
    </linearGradient>
  </defs>
  <rect x="0" y="22" width="640" height="503" fill="#141414"/>
  <polygon points="573,0 1200,0 1200,547 645,547" fill="url(#welcomePhoto)" role="img" aria-label="Open electrical cabinet and site supervisor reviewing plans"/>
  <polygon points="561,88 580,88 640,525 620,525" fill="#1f9a3b"/>
</svg>
<h2 class="abs display welcome-title">Welcome to<br>Harbor Oak<br>Electric</h2>
<p class="abs welcome-text">Sed ut perspiciatis unde omnis iste natus error sit voluptatem accusantium doloremque laudantium, totam rem aperiam, eaque ipsa quae ab illo inventore veritatis et quasi architecto beatae vitae dicta sunt explicabo. Nemo enim ipsam voluptatem quia voluptas.</p>
<div class="btn welcome-btn">Read More</div>

<!-- what we do -->
<h2 class="display section-title" style="top:2060px">What We Do</h2>
<ul class="checklist" style="left:75px">
  <li><svg width="18" height="18" viewBox="0 0 18 18"><circle cx="9" cy="9" r="9" fill="#1f9a3b"/><path d="m7 5 4 4-4 4" fill="none" stroke="#fff" stroke-width="2"/></svg>Sed ut perspiciatis unde</li>
  <li><svg width="18" height="18" viewBox="0 0 18 18"><circle cx="9" cy="9" r="9" fill="#1f9a3b"/><path d="m7 5 4 4-4 4" fill="none" stroke="#fff" stroke-width="2"/></svg>Qmnis iste natus error sit voluptatem</li>
  <li><svg width="18" height="18" viewBox="0 0 18 18"><circle cx="9" cy="9" r="9" fill="#1f9a3b"/><path d="m7 5 4 4-4 4" fill="none" stroke="#fff" stroke-width="2"/></svg>Accusantium doloremque</li>
  <li><svg width="18" height="18" viewBox="0 0 18 18"><circle cx="9" cy="9" r="9" fill="#1f9a3b"/><path d="m7 5 4 4-4 4" fill="none" stroke="#fff" stroke-width="2"/></svg>Laudantium, totam rem</li>
  <li><svg width="18" height="18" viewBox="0 0 18 18"><circle cx="9" cy="9" r="9" fill="#1f9a3b"/><path d="m7 5 4 4-4 4" fill="none" stroke="#fff" stroke-width="2"/></svg>Aperiameaque ipsa quae</li>
  <li><svg width="18" height="18" viewBox="0 0 18 18"><circle cx="9" cy="9" r="9" fill="#1f9a3b"/><path d="m7 5 4 4-4 4" fill="none" stroke="#fff" stroke-width="2"/></svg>Inventore veritatis</li>
  <li><svg width="18" height="18" viewBox="0 0 18 18"><circle cx="9" cy="9" r="9" fill="#1f9a3b"/><path d="m7 5 4 4-4 4" fill="none" stroke="#fff" stroke-width="2"/></svg>Quasi architecto beatae vitae</li>
  <li><svg width="18" height="18" viewBox="0 0 18 18"><circle cx="9" cy="9" r="9" fill="#1f9a3b"/><path d="m7 5 4 4-4 4" fill="none" stroke="#fff" stroke-width="2"/></svg>Dicta sunt explicabo</li>
</ul>
<ul class="checklist" style="left:442px">
  <li><svg width="18" height="18" viewBox="0 0 18 18"><circle cx="9" cy="9" r="9" fill="#1f9a3b"/><path d="m7 5 4 4-4 4" fill="none" stroke="#fff" stroke-width="2"/></svg>Sed ut perspiciatis unde</li>
  <li><svg width="18" height="18" viewBox="0 0 18 18"><circle cx="9" cy="9" r="9" fill="#1f9a3b"/><path d="m7 5 4 4-4 4" fill="none" stroke="#fff" stroke-width="2"/></svg>Qmnis iste natus error sit voluptatem</li>
  <li><svg width="18" height="18" viewBox="0 0 18 18"><circle cx="9" cy="9" r="9" fill="#1f9a3b"/><path d="m7 5 4 4-4 4" fill="none" stroke="#fff" stroke-width="2"/></svg>Accusantium doloremque</li>
  <li><svg width="18" height="18" viewBox="0 0 18 18"><circle cx="9" cy="9" r="9" fill="#1f9a3b"/><path d="m7 5 4 4-4 4" fill="none" stroke="#fff" stroke-width="2"/></svg>Laudantium, totam rem</li>
  <li><svg width="18" height="18" viewBox="0 0 18 18"><circle cx="9" cy="9" r="9" fill="#1f9a3b"/><path d="m7 5 4 4-4 4" fill="none" stroke="#fff" stroke-width="2"/></svg>Aperiameaque ipsa quae</li>
  <li><svg width="18" height="18" viewBox="0 0 18 18"><circle cx="9" cy="9" r="9" fill="#1f9a3b"/><path d="m7 5 4 4-4 4" fill="none" stroke="#fff" stroke-width="2"/></svg>Inventore veritatis</li>
  <li><svg width="18" height="18" viewBox="0 0 18 18"><circle cx="9" cy="9" r="9" fill="#1f9a3b"/><path d="m7 5 4 4-4 4" fill="none" stroke="#fff" stroke-width="2"/></svg>Quasi architecto beatae vitae</li>
  <li><svg width="18" height="18" viewBox="0 0 18 18"><circle cx="9" cy="9" r="9" fill="#1f9a3b"/><path d="m7 5 4 4-4 4" fill="none" stroke="#fff" stroke-width="2"/></svg>Dicta sunt explicabo</li>
</ul>
<ul class="checklist" style="left:809px">
  <li><svg width="18" height="18" viewBox="0 0 18 18"><circle cx="9" cy="9" r="9" fill="#1f9a3b"/><path d="m7 5 4 4-4 4" fill="none" stroke="#fff" stroke-width="2"/></svg>Sed ut perspiciatis unde</li>
  <li><svg width="18" height="18" viewBox="0 0 18 18"><circle cx="9" cy="9" r="9" fill="#1f9a3b"/><path d="m7 5 4 4-4 4" fill="none" stroke="#fff" stroke-width="2"/></svg>Qmnis iste natus error sit voluptatem</li>
  <li><svg width="18" height="18" viewBox="0 0 18 18"><circle cx="9" cy="9" r="9" fill="#1f9a3b"/><path d="m7 5 4 4-4 4" fill="none" stroke="#fff" stroke-width="2"/></svg>Accusantium doloremque</li>
  <li><svg width="18" height="18" viewBox="0 0 18 18"><circle cx="9" cy="9" r="9" fill="#1f9a3b"/><path d="m7 5 4 4-4 4" fill="none" stroke="#fff" stroke-width="2"/></svg>Laudantium, totam rem</li>
  <li><svg width="18" height="18" viewBox="0 0 18 18"><circle cx="9" cy="9" r="9" fill="#1f9a3b"/><path d="m7 5 4 4-4 4" fill="none" stroke="#fff" stroke-width="2"/></svg>Aperiameaque ipsa quae</li>
  <li><svg width="18" height="18" viewBox="0 0 18 18"><circle cx="9" cy="9" r="9" fill="#1f9a3b"/><path d="m7 5 4 4-4 4" fill="none" stroke="#fff" stroke-width="2"/></svg>Inventore veritatis</li>
  <li><svg width="18" height="18" viewBox="0 0 18 18"><circle cx="9" cy="9" r="9" fill="#1f9a3b"/><path d="m7 5 4 4-4 4" fill="none" stroke="#fff" stroke-width="2"/></svg>Quasi architecto beatae vitae</li>
  <li><svg width="18" height="18" viewBox="0 0 18 18"><circle cx="9" cy="9" r="9" fill="#1f9a3b"/><path d="m7 5 4 4-4 4" fill="none" stroke="#fff" stroke-width="2"/></svg>Dicta sunt explicabo</li>
</ul>
<div class="btn services-btn">View All Services</div>

<!-- testimonials -->
<div class="abs testimonials" role="img" aria-label="Green-tinted background of circuit breaker switches"></div>
<h2 class="display section-title testi-title">Testimonials</h2>
<svg class="arrow" style="left:36px;top:2874px" width="24" height="40" viewBox="0 0 24 40"><path d="M20 2 3 20l17 18" fill="none" stroke="#fff" stroke-width="3"/></svg>
<svg class="arrow" style="left:1140px;top:2874px" width="24" height="40" viewBox="0 0 24 40"><path d="m4 2 17 18L4 38" fill="none" stroke="#fff" stroke-width="3"/></svg>
<div class="testi" style="left:75px">
  <div class="testi-photo" role="img" aria-label="Portrait of a smiling male client"></div>
  <h4>Name Heading</h4>
  <p>Vestibulum ante ipsum primis in faucibus orci luctus et ultrices posuere cubilia lobortis turpis in odio blandit aliquam nibh</p>
</div>
<div class="testi" style="left:435px">
  <div class="testi-photo" role="img" aria-label="Portrait of a female client"></div>
  <h4>Name Heading</h4>
  <p>Vestibulum ante ipsum primis in faucibus orci luctus et ultrices posuere cubilia lobortis turpis in odio blandit aliquam nibh</p>
</div>
<div class="testi" style="left:795px">
  <div class="testi-photo" role="img" aria-label="Portrait of a smiling female client"></div>
  <h4>Name Heading</h4>
  <p>Vestibulum ante ipsum primis in faucibus orci luctus et ultrices posuere cubilia lobortis turpis in odio blandit aliquam nibh</p>
</div>

<!-- subscribe -->
<h2 class="display section-title sub-title">Email Subscribe</h2>
<p class="abs sub-text">Vestibulum ante ipsum primis in faucibus orci luctus et ultrices posuere cubilia lobortis turpis in odio blandit aliquam nibh</p>
<div class="abs sub-form">
  <div class="sub-input">
    <svg width="15" height="12" viewBox="0 0 15 12"><rect width="15" height="12" rx="1" fill="#444"/><path d="m1 1 6.5 5L14 1" fill="none" stroke="#f1f1f1" stroke-width="1.4"/></svg>
    Enter Email Address
  </div>
  <div class="btn sub-btn">Sign Up</div>
</div>

<!-- footer -->
<footer class="abs footer"></footer>
<div class="abs f-head" style="left:75px">Site Map</div>
<ul class="abs f-list" style="left:75px"><li>Home</li><li>About Us</li><li>Services</li><li>Commercial</li><li>Residential</li></ul>
<ul class="abs f-list" style="left:217px"><li>Testimonials</li><li>Blog</li><li>Contact Us</li></ul>
<div class="abs f-head" style="left:369px">Services</div>
<ul class="abs f-list" style="left:369px"><li>Sed ut perspiciatis</li><li>Unde omnis iste</li><li>Natus error sit voluptatem</li><li>Accusantium</li><li>Nemo enim ipsam</li></ul>
<div class="abs f-head" style="left:615px">Contact Info</div>
<div class="abs f-contact">
  <div class="name">Harbor Oak Electric</div>
  <div>480 Maple Crest Rd #12,<br>Cary, NC 27511</div>
  <div class="row" style="margin-top:4px"><svg width="12" height="12" viewBox="0 0 24 24"><path fill="#ccc" d="M6.6 10.8a15.1 15.1 0 0 0 6.6 6.6l2.2-2.2c.3-.3.7-.4 1-.2 1.1.4 2.3.6 3.6.6.6 0 1 .4 1 1V20c0 .6-.4 1-1 1A17 17 0 0 1 3 4c0-.6.4-1 1-1h3.5c.6 0 1 .4 1 1 0 1.3.2 2.5.6 3.6.1.3 0 .7-.2 1z"/></svg>1-800-555-0142</div>
  <div class="row"><svg width="13" height="10" viewBox="0 0 15 12"><rect width="15" height="12" rx="1" fill="#ccc"/><path d="m1 1 6.5 5L14 1" fill="none" stroke="#1b1b1b" stroke-width="1.4"/></svg>hello@harboroakelectric.com</div>
</div>
<div class="abs f-head" style="left:887px">Follow Us</div>
<div class="abs socials"><span></span><span></span><span></span><span></span><span></span></div>
<div class="abs f-brand"><div class="n">HARBOR OAK</div><div class="s">ELECTRIC</div></div>
<div class="abs footer-bottom">Copyright © 2021 Company Name All Right Reserved</div>

</body>
</html>
```